Brantley Studios photography and video creator

I need a business card for my production company. I shoot photography and videography for real estate, adventure sports and businesses

Contact Information for Business Card

simple not to busy

Colors

Designer to choose colors to be used in the design.

Requirements
Must have
• derek@brantleystudios.ca
• phone -5873304127
• instagram derek_brantley

```html
<!DOCTYPE html>
<html lang="en">
<head>
<meta charset="utf-8">
<title>Brantley Studios — Business Card</title>
<link href="https://fonts.googleapis.com/css2?family=Open+Sans:wght@400;600;700&display=swap" rel="stylesheet">
<style>
  :root {
    --backdrop: #2a2a2a;
    --card: #ffffff;
    --ink: #111111;
    --ink-soft: #333333;
    --mark: #1a1a1a;
  }
  * { box-sizing: border-box; margin: 0; padding: 0; }
  html, body {
    width: 1200px; height: 900px; overflow: hidden;
    background: var(--backdrop);
    font-family: "Open Sans", Arial, sans-serif;
    color: var(--ink);
  }
  .stage {
    width: 1200px; height: 900px;
    display: flex; flex-direction: column; align-items: center; justify-content: center;
    gap: 36px;
  }
  .card {
    width: 680px; height: 388px;
    background: var(--card);
    position: relative;
    box-shadow: 0 10px 30px rgba(0,0,0,.45);
  }
  .brand {
    display: flex; align-items: center; gap: 22px;
  }
  .brand-dot {
    border-radius: 50%;
    background: var(--mark);
    flex: none;
  }
  .brand-name {
    font-weight: 700;
    text-transform: uppercase;
    letter-spacing: .04em;
    color: var(--ink);
    line-height: 1.1;
  }
  .card--front {
    display: flex; align-items: center; justify-content: center;
  }
  .card--front .brand-dot { width: 190px; height: 190px; }
  .card--front .brand-name { font-size: 40px; }

  .card--back .brand {
    position: absolute; left: 44px; top: 50%; transform: translateY(-50%);
    flex-direction: column; gap: 14px;
  }
  .card--back .brand-dot { width: 150px; height: 150px; }
  .card--back .brand-name { font-size: 20px; text-align: center; }

  .divider {
    position: absolute; left: 300px; top: 112px;
    width: 3px; height: 170px; background: var(--ink);
  }
  .details {
    position: absolute; left: 338px; top: 96px;
  }
  .person-name {
    font-size: 30px; font-weight: 400; text-transform: uppercase; line-height: 1;
  }
  .person-name strong { font-weight: 700; }
  .person-role {
    font-size: 15px; text-transform: uppercase; color: var(--ink-soft);
    margin: 6px 0 0 30px;
  }
  .contact-list {
    list-style: none; margin-top: 26px;
  }
  .contact-list li {
    display: flex; align-items: center; gap: 24px;
    font-size: 15px; color: var(--ink-soft);
    height: 36px;
  }
  .contact-list svg { width: 22px; height: 22px; flex: none; }
</style>
</head>
<body>
<main class="stage">
  <section class="card card--front" aria-label="Card front">
    <div class="brand">
      <span class="brand-dot"></span>
      <span class="brand-name">Brantley<br>Studios</span>
    </div>
  </section>

  <section class="card card--back" aria-label="Card back">
    <div class="brand">
      <span class="brand-dot"></span>
      <span class="brand-name">Brantley Studios</span>
    </div>
    <span class="divider"></span>
    <div class="details">
      <h1 class="person-name"><strong>Derek</strong> Brantley</h1>
      <p class="person-role">Owner</p>
      <ul class="contact-list">
        <li>
          <svg viewBox="0 0 24 24" aria-hidden="true"><path d="M6.6 10.8a15 15 0 0 0 6.6 6.6l2.2-2.2a1 1 0 0 1 1-.25 11 11 0 0 0 3.6.6 1 1 0 0 1 1 1V20a1 1 0 0 1-1 1A17 17 0 0 1 3 4a1 1 0 0 1 1-1h3.5a1 1 0 0 1 1 1c0 1.25.2 2.45.6 3.6a1 1 0 0 1-.25 1z" fill="#111"/></svg>
          <span>5873304127</span>
        </li>
        <li>
          <svg viewBox="0 0 24 24" aria-hidden="true"><rect x="2.5" y="5" width="19" height="14" fill="none" stroke="#111" stroke-width="1.6"/><path d="M2.5 5l9.5 8 9.5-8" fill="none" stroke="#111" stroke-width="1.6"/></svg>
          <span>derek@brantleystudios.ca</span>
        </li>
        <li>
          <svg viewBox="0 0 24 24" aria-hidden="true"><circle cx="12" cy="12" r="10" fill="#111"/></svg>
          <span>instagram derek_brantley</span>
        </li>
      </ul>
    </div>
  </section>
</main>
</body>
</html>
```